Business card

I need a business card design for my consulting company in animal welfare for livestock. I like clean, crisp, simple.

One I imagined was double-sided:
side1: just my name and contact information
side2: silhouette of farm animals. Could be 3 (pig, cow, chicken) or all the species (pig, cow, chicken, duck, sheep, rabbit, etc) that continue the length of the card. I have attached an image of a silhouette style.

But, I am open to any concept.

```html
<!DOCTYPE html>
<html lang="en">
<head>
<meta charset="utf-8">
<title>Clara Westbrook – Business Card</title>
<link rel="stylesheet" href="https://fonts.googleapis.com/css2?family=Kreon:wght@500&family=Arimo:wght@700&family=Tinos:wght@700&display=swap">
<style>
  :root {
    --page-bg: #e9e6e2;
    --green-light: #7cc22a;
    --green-mid: #1f9a3c;
    --green-dark: #0b6e36;
    --band-green: #0f9a45;
    --band-navy: #2c1b78;
    --tagline-yellow: #f5f00f;
    --name-ink: #0f1a12;
    --contact-ink: #ffffff;
    --silhouette: #ffffff;
  }
  * { margin: 0; padding: 0; box-sizing: border-box; }
  html, body {
    width: 1200px; height: 888px; overflow: hidden;
    background: var(--page-bg);
  }
  .canvas { position: relative; width: 1200px; height: 888px; }

  .card {
    position: absolute;
    width: 640px; height: 376px;
    background: radial-gradient(ellipse 60% 70% at 50% 50%, var(--green-light) 0%, var(--green-mid) 55%, var(--green-dark) 100%);
    box-shadow: 0 6px 18px rgba(0,0,0,.25);
    overflow: hidden;
  }
  .card--front { left: 60px; top: 50px; }
  .card--back  { left: 500px; top: 462px; }

  .card__name {
    position: absolute; left: 0; right: 0; top: 108px;
    text-align: center;
    font-family: "Kreon", Georgia, serif;
    font-weight: 500; font-size: 40px;
    color: var(--name-ink);
  }
  .card__band-rule {
    position: absolute; left: 0; right: 0;
    height: 10px; background: var(--band-green);
  }
  .card__band-rule--top { top: 176px; }
  .card__band-rule--bottom { top: 235px; }
  .card__tagline-band {
    position: absolute; left: 0; right: 0; top: 186px; height: 49px;
    background: var(--band-navy);
    display: flex; align-items: center; justify-content: center;
  }
  .card__tagline {
    font-family: "Arimo", Arial, sans-serif;
    font-weight: 700; font-size: 24px;
    color: var(--tagline-yellow);
  }
  .card__contact {
    position: absolute; left: 148px; top: 254px;
    font-family: "Tinos", "Times New Roman", serif;
    font-weight: 700; font-size: 21px; line-height: 25px;
    color: var(--contact-ink);
  }
  .card__contact-row { display: flex; }
  .card__contact-label { width: 64px; }

  .card__artwork {
    position: absolute; left: 205px; top: 38px;
    width: 390px; height: 260px;
    border-radius: 40px 60px 20px 20px;
    background: var(--silhouette);
  }
</style>
</head>
<body>
<main class="canvas">
  <section class="card card--front" aria-label="Business card front">
    <h1 class="card__name">Clara Westbrook</h1>
    <div class="card__band-rule card__band-rule--top"></div>
    <div class="card__tagline-band">
      <p class="card__tagline">Welfare Services for Livestock Stakeholders</p>
    </div>
    <div class="card__band-rule card__band-rule--bottom"></div>
    <div class="card__contact">
      <div class="card__contact-row"><span class="card__contact-label">Email</span><span>: clara.westbrook@mail.example</span></div>
      <div class="card__contact-row"><span class="card__contact-label">Tel</span><span>: +1.555.204.7716</span></div>
    </div>
  </section>

  <section class="card card--back" aria-label="Business card back">
    <div class="card__artwork" role="img" aria-label="White silhouette of a dairy cow standing in grass"></div>
  </section>
</main>
</body>
</html>
```